Business Card

I need a business card for my work as an energy lawyer. I am a single prctioner and I consult to energy companies regarding a variety of legal issues involving environmental matters, energy efficiency, regulations and contractual arrangements. i need a distinctive business card that stands out and is easy to read. I like bold colors or high contrast. I like a sparse architectural design. The font should be easy to read (many of my clients use reading glasses and are concerned about small type). The card should communicate that I am somewhat different from ordinary legal counsel. Below are some examples of cards that I like. Thank you for your interest and thought. Glenn Dusty Harker
Updates

Thanks to everyone who has submitted a design.  My general comments are:

1.  I like the colourful cards and the high contrast cards.
2.  I prefer the use of icons for home address, phone, mobile and email.
3.  For the high contrast cards please use three colours - black background, and red and white for the logo or information.
4.  The mobile number area code should be 403 and not 404.
5.  I also need to add a direct phone line which is 403-517-6392.

Thank you,

Glenn Harker

Reason: I have briefly extended the deadline by three days to allow those individuals who responded early to revise their designs based upon the subsequent clarification of the colours (red, white, black background) and the request to use icons and add a direct phone number.

Industry/Entity Type

Business

```html
<!DOCTYPE html>
<html lang="en">
<head>
<meta charset="utf-8">
<title>Glenn Dusty Harker – Business Card</title>
<link rel="stylesheet" href="https://fonts.googleapis.com/css2?family=Ubuntu:wght@300;400;500;700&display=swap">
<style>
  :root {
    --backdrop: #d9d6d0;
    --card-black: #2a2928;
    --card-cream: #ece8dc;
    --accent-red: #e0202a;
    --ink-white: #f2f2f2;
    --ink-grey: #c9c9c9;
    --ink-dark: #2b2a29;
  }
  * { margin: 0; padding: 0; box-sizing: border-box; }
  html, body { width: 1200px; height: 900px; overflow: hidden; }
  body {
    background: var(--backdrop);
    font-family: "Ubuntu", sans-serif;
    display: flex;
    flex-direction: column;
    align-items: center;
    justify-content: center;
    gap: 60px;
  }
  .card {
    position: relative;
    width: 600px;
    height: 343px;
    border-radius: 4px;
    box-shadow: 0 6px 18px rgba(0,0,0,.18);
    overflow: hidden;
  }

  /* Front */
  .card-front { background: var(--card-black); color: var(--ink-white); }
  .front-name {
    position: absolute;
    left: 168px;
    top: 118px;
    font-size: 30px;
    letter-spacing: 5px;
    white-space: nowrap;
  }
  .front-name .given { font-weight: 300; }
  .front-name .family { font-weight: 700; letter-spacing: 4px; }
  .front-title {
    position: absolute;
    left: 168px;
    top: 160px;
    font-size: 17px;
    font-weight: 400;
    color: var(--ink-grey);
  }
  .front-rule {
    position: absolute;
    left: 40px;
    top: 232px;
    width: 400px;
    height: 4px;
    background: var(--accent-red);
  }

  /* Back */
  .card-back { background: var(--card-cream); color: var(--ink-dark); }
  .back-name {
    position: absolute;
    left: 40px;
    top: 34px;
    font-size: 20px;
    font-weight: 400;
  }
  .contact-list {
    position: absolute;
    list-style: none;
    font-size: 14px;
    line-height: 22px;
  }
  .contact-list li { display: flex; align-items: center; gap: 8px; }
  .contact-list svg { width: 12px; height: 12px; fill: var(--accent-red); flex: none; }
  .contact-personal { left: 40px; top: 76px; }
  .contact-office { left: 300px; top: 112px; }
  .back-rule {
    position: absolute;
    left: 0;
    top: 252px;
    width: 430px;
    height: 4px;
    background: var(--accent-red);
  }
  .back-signature {
    position: absolute;
    right: 170px;
    top: 222px;
    font-size: 20px;
    font-weight: 400;
  }
  .back-address {
    position: absolute;
    left: 150px;
    top: 266px;
    font-size: 15px;
    font-weight: 400;
  }
</style>
</head>
<body>

  <section class="card card-front" aria-label="Card front">
    <h1 class="front-name"><span class="given">GLENN</span> <span class="family">D.HARKER</span></h1>
    <p class="front-title">Barrister and Solicitor, LLB, ICD.D</p>
    <div class="front-rule"></div>
  </section>

  <section class="card card-back" aria-label="Card back">
    <h2 class="back-name">Glenn Dusty Harker</h2>

    <ul class="contact-list contact-personal">
      <li>
        <svg viewBox="0 0 12 12" aria-label="Phone"><path d="M2.5 0.5 L4.5 0.5 L5 3.5 L3.6 4.4 Q4.6 6.8 7.3 8.3 L8.3 7 L11.5 7.5 L11.5 9.6 Q11 11.5 9 11.5 Q0.5 10 0.5 2.5 Q0.6 0.7 2.5 0.5 Z"/></svg>
        1.403.682.1935
      </li>
      <li>
        <svg viewBox="0 0 12 12" aria-label="Mobile"><path d="M3 0.5 H9 V11.5 H3 Z M4 1.8 V8.8 H8 V1.8 Z"/></svg>
        1.403.829.4107
      </li>
    </ul>

    <ul class="contact-list contact-office">
      <li>
        <svg viewBox="0 0 12 12" aria-label="Direct phone"><path d="M2.5 0.5 L4.5 0.5 L5 3.5 L3.6 4.4 Q4.6 6.8 7.3 8.3 L8.3 7 L11.5 7.5 L11.5 9.6 Q11 11.5 9 11.5 Q0.5 10 0.5 2.5 Q0.6 0.7 2.5 0.5 Z"/></svg>
        1.403.517.6392 (DIRECT)
      </li>
      <li>
        <svg viewBox="0 0 12 12" aria-label="Email"><path d="M0.5 2.5 H11.5 V10 H0.5 Z M1.5 3.3 L6 6.8 L10.5 3.3 Z"/></svg>
        dusty@dustyharker.com
      </li>
    </ul>

    <p class="back-signature">Glenn Dusty Harker</p>
    <div class="back-rule"></div>
    <p class="back-address">2140 9th Avenue S.W., Calgary, Alberta</p>
  </section>

</body>
</html>
```